Web Design Project

We need a logo, web site and business cards for our new business, Velquist Optics. We specialize in aerial videography and photography via drone. Currently we are mainly focusing on real estate videography but will branch into other markets and may even host training classes for flying drones.
Updates

Target Market(s)

Real estate agents, property managers, hotels and customers looking to learn how to fly drones.

Industry/Entity Type

Videography

Font styles to use
Sans Serif

Colors

Designer to choose colors to be used in the design.

Requirements
Must have
• Space for video feed on home page
A page for completed projects
A page for training classes
About us page

```html
<!DOCTYPE html>
<html lang="en">
<head>
<meta charset="utf-8">
<title>Velquist Optics</title>
<link rel="stylesheet" href="https://fonts.googleapis.com/css2?family=Libre+Franklin:wght@400;500;600&display=swap">
<style>
:root{
  --orange:#f29a0e;
  --orange-dark:#e08a00;
  --ink:#333;
  --muted:#555;
  --soft:#f4f3f1;
  --line:#d8d8d8;
  --footer-top:#5a5a5a;
  --footer-bottom:#2e2e2e;
  --hero-band:rgba(40,55,20,.82);
}
*{box-sizing:border-box;margin:0;padding:0}
html,body{width:754px;height:1200px;overflow:hidden}
body{position:relative;background:#fff;font-family:"Libre Franklin",Arial,sans-serif;color:var(--ink)}
.abs{position:absolute}
.accent{color:var(--orange)}

.header{top:0;left:0;width:754px;height:70px;background:#fff}
.brand{left:83px;top:18px;display:flex;align-items:center;gap:8px}
.brand-mark{width:30px;height:30px;background:var(--orange)}
.brand-name{font-size:20px;font-weight:500;color:#222;letter-spacing:.5px}
.nav{right:94px;top:30px;display:flex;gap:15px;align-items:center;font-size:8px;color:#444}
.nav a{color:inherit;text-decoration:none;padding:5px 0}
.nav a.active{border:1.5px solid var(--orange);color:var(--orange);padding:5px 9px}

.hero{top:70px;left:0;width:754px;height:284px;background:linear-gradient(180deg,#587a2e 0%,#6f8f3e 40%,#8aa24e 75%,#7a8e42 100%)}
.hero-drone{left:318px;top:52px;width:400px;height:190px;border-radius:40px;background:radial-gradient(ellipse at center,rgba(240,240,240,.75),rgba(240,240,240,0) 70%)}
.hero-line{left:82px;background:var(--hero-band);color:#fff;font-size:18px;padding:2px 15px 3px;white-space:nowrap}
.hero-line.one{top:113px}
.hero-line.two{top:148px}

.dots{top:366px;left:356px;display:flex;gap:4px}
.dots span{width:8px;height:8px;border-radius:50%;background:#ccc}
.dots span.on{background:var(--orange)}

.welcome{top:410px;left:0;width:754px;text-align:center}
.section-title{font-size:18px;font-weight:400;color:#333}
.welcome p{width:590px;margin:12px auto 0;font-size:7.6px;line-height:15.6px;color:var(--muted)}
.btn{display:inline-block;margin-top:16px;background:var(--orange);color:#fff;font-size:8px;padding:8px 15px;width:73px;text-align:center}

.video{top:554px;left:0;width:754px;height:240px;background:var(--soft)}
.video .section-title{position:absolute;top:30px;width:100%;text-align:center}
.video-text{left:83px;top:76px;width:330px}
.video-text h3{font-size:11px;font-weight:500;letter-spacing:.2px;color:#222}
.video-text p{margin-top:12px;font-size:7.6px;line-height:15.7px;color:var(--muted)}
.meta{margin-top:18px;width:138px;list-style:none;font-size:7.6px;color:var(--orange)}
.meta li{border-top:1px solid var(--line);padding:5px 0 5px 4px}
.meta li:last-child{border-bottom:1px solid var(--line)}
.meta li::before{content:"";display:inline-block;border-left:4px solid var(--orange);border-top:2.5px solid transparent;border-bottom:2.5px solid transparent;margin-right:7px}
.video-frame{left:434px;top:66px;width:238px;height:138px;border:2px solid #e2e2e2;background:linear-gradient(160deg,#7d8a88 0%,#5f6a66 45%,#4e5a3e 100%)}
.play{left:96px;top:47px}

.works{top:820px;left:0;width:754px;text-align:center}
.work{top:46px;width:179px;text-align:left}
.work .thumb{height:100px;border:2px solid #ddd}
.work p{margin-top:13px;padding-left:2px;font-size:7.6px;line-height:13.5px;color:var(--muted)}
.w1{left:85px}.w2{left:288px}.w3{left:490px}
.w1 .thumb{background:linear-gradient(135deg,#6d5a2c,#3d4a2a 50%,#8a7a4a)}
.w2 .thumb{background:linear-gradient(180deg,#9aa6ad,#4f6238 40%,#6f8a45)}
.w3 .thumb{background:linear-gradient(180deg,#8aa0a8,#6f8c4a 35%,#c99a62 70%,#d8a66a)}

.footer{top:1041px;left:0;width:754px;height:159px;background:linear-gradient(180deg,var(--footer-top),var(--footer-bottom));color:#eee}
.footer h4{font-size:13px;font-weight:400;color:#f2f2f2}
.f-about{left:84px;top:34px;width:180px}
.f-about p{margin-top:12px;font-size:7.6px;line-height:15.2px;color:#ddd}
.f-about a{display:block;margin-top:4px;font-size:7.6px;color:var(--orange);text-decoration:none}
.f-links{left:288px;top:35px}
.link-cols{display:flex;gap:34px;margin-top:11px}
.link-cols ul{list-style:none;width:84px;font-size:7.6px;color:#eee}
.link-cols li{border-bottom:1px solid #777;padding:5px 0 5px 12px;position:relative}
.link-cols li::before{content:"";position:absolute;left:2px;top:8px;border-left:4px solid #eee;border-top:2.5px solid transparent;border-bottom:2.5px solid transparent}
.f-contact{left:538px;top:35px}
.social{display:flex;gap:4px;margin-top:14px}
.social span{width:19px;height:19px;border-radius:50%;background:#fff}
.copy{margin-top:20px;font-size:7.4px;line-height:12px;color:#ddd}
</style>
</head>
<body>

<header class="abs header">
  <div class="abs brand"><span class="brand-mark"></span><span class="brand-name">Velquist Optics</span></div>
  <nav class="abs nav">
    <a class="active" href="#">Home</a>
    <a href="#">About us</a>
    <a href="#">Videos</a>
    <a href="#">Completed Projects</a>
    <a href="#">Training Classes</a>
    <a href="#">Contact us</a>
  </nav>
</header>

<section class="abs hero">
  <div class="abs hero-drone" role="img" aria-label="White quadcopter drone with a camera mounted underneath, flying over a blurred green field"></div>
  <div class="abs hero-line one">We specialise in aerial videography</div>
  <div class="abs hero-line two">and photography via drone.</div>
</section>

<div class="abs dots"><span class="on"></span><span></span><span></span><span></span></div>

<section class="abs welcome">
  <h2 class="section-title">Welcome to Our <span class="accent">Site!</span></h2>
  <p>Lorem ipsum dolor sit amet, consectetur adipiscing elit, sed do eiusmod tempor incididunt ut labore et dolore magna aliqua. Ut enim ad minim veniam, quis nostrud exercitation ullamco laboris nisi ut aliquip ex ea commodo consequat. Lorem ipsum dolor sit amet, consectetur adipiscing elit, sed do eiusmod tempor incididunt ut labore et dolore magna aliqua. Ut enim ad minim veniam,</p>
  <span class="btn">Read More</span>
</section>

<section class="abs video">
  <h2 class="section-title"><span class="accent">Video</span> Feed</h2>
  <div class="abs video-text">
    <h3>DUIS AUTE IRURE DOLOR IN VOLUPTATE</h3>
    <p>Lorem ipsum dolor sit amet, consectetur adipiscing elit, sed do eiusmod tempor incidi dunt ut labore et dolore magna aliqua. Ut enim ad minim veniam, quis nostrud exercita tion ullamco laboris nisi ut aliquip ex ea commodo consequat.</p>
    <ul class="meta">
      <li>Fed by Dorian</li>
      <li>Fed at 110,829&nbsp; Views</li>
    </ul>
  </div>
  <div class="abs video-frame" role="img" aria-label="Aerial video still of a curving residential street lined with townhomes">
    <svg class="abs play" width="44" height="44" viewBox="0 0 44 44" aria-hidden="true">
      <circle cx="22" cy="22" r="19.5" fill="none" stroke="#fff" stroke-width="3"/>
      <path d="M17 13 L31 22 L17 31 Z" fill="#fff"/>
    </svg>
  </div>
</section>

<section class="abs works">
  <h2 class="section-title">Our <span class="accent">Works</span></h2>
  <div class="abs work w1">
    <div class="thumb" role="img" aria-label="Aerial photo of a stone manor beside a pond among autumn trees"></div>
    <p>Ut enim ad minim veniam, quis nostrud exerc tion ullamco laboris nisi ut aliquip</p>
  </div>
  <div class="abs work w2">
    <div class="thumb" role="img" aria-label="Aerial photo of a suburban neighbourhood with large homes and lawns"></div>
    <p>Ut enim ad minim veniam, quis nostrud exerc tion ullamco laboris nisi ut aliquip</p>
  </div>
  <div class="abs work w3">
    <div class="thumb" role="img" aria-label="Aerial photo of a ranch building with sand riding arenas"></div>
    <p>Ut enim ad minim veniam, quis nostrud exerc tion ullamco laboris nisi ut aliquip</p>
  </div>
</section>

<footer class="abs footer">
  <div class="abs f-about">
    <h4>About Us</h4>
    <p>Lorem ipsum dolor sit amet, consectetur adips cing elit, sed do eiusmod tempor incididunt ut labore et dolore magna aliqua</p>
    <a href="#">Read More</a>
  </div>
  <div class="abs f-links">
    <h4>Useful Links</h4>
    <div class="link-cols">
      <ul><li>Home</li><li>About us</li><li>Videos</li><li>Completed Projects</li></ul>
      <ul><li>Training Classes</li><li>Contact us</li></ul>
    </div>
  </div>
  <div class="abs f-contact">
    <h4>Get In Touch</h4>
    <div class="social"><span></span><span></span><span></span><span></span><span></span></div>
    <p class="copy">Copyright ©2014 . Velquistoptics.<br>All Right Reserved.</p>
  </div>
</footer>

</body>
</html>
```